International Medical Company Needs a Website Design for a Support Site

We need a website design for a support site we are doing for ostomates called Bright Returns. We are an international company but this website is for our Australian market.

The website is a support site for people who are living with an Ostomy or Bowel Disease. This is a site where they can read other ostomates' stories and how they are dealing with the fact that they have to wear a pouch everyday.

The URL for our US site is: http://www.brightreturnsvale.com/

We need to use the same logo but we have freedom around the color scheme. We are not fond of the brown color scheme used in our US site and are happy for designs to be submitted with alternatives.

• We want the design to be clean, inspiring, modern and inviting.
• We would like to see a design for the mainpage / homepage and one of the subpages
• We only require the PSD / image files (no HTML needed)

Attached to this project is our sitemap, an example wireframe and the logos. We are happy for you to play around with different options and don't have to stick to the layout shown in the wireframe.

If you have any further questions please ask.

```html
<!DOCTYPE html>
<html lang="en">
<head>
<meta charset="utf-8">
<title>Bright Returns – Sharing Stories &amp; Giving Hope</title>
<link rel="stylesheet" href="https://fonts.googleapis.com/css2?family=Roboto+Condensed:wght@400;700&family=Roboto:ital,wght@0,300;0,400;0,700;1,300;1,400&display=swap">
<style>
:root{
  --navy:#13288a;
  --nav:#1c3b95;
  --brown:#8a4a14;
  --brown-dark:#5e2f0c;
  --brown-light:#a8672f;
  --blue:#0b7fd0;
  --blue-dark:#0d2f8f;
  --beige:#efe6de;
  --sky:#cfe8f6;
  --sky-pale:#f1f8fc;
  --green:#bfe39a;
  --green-pale:#eef8e0;
  --text:#333;
  --rule:#8a4a14;
}
*{margin:0;padding:0;box-sizing:border-box}
html,body{width:1200px;height:847px;overflow:hidden;background:#fff}
body{position:relative;font-family:"Roboto",Arial,sans-serif;color:var(--text)}
.abs{position:absolute}

/* header */
.header-band{left:0;top:43px;width:1200px;height:44px;border-top:1px solid #cfe6f4;
  background:linear-gradient(#f4fafd,#cfe8f6)}
.brand{left:150px;top:0;width:171px;height:112px;background:#fff;
  display:flex;flex-direction:column;align-items:center;justify-content:flex-end;padding-bottom:16px;gap:10px}
.brand-mark{width:44px;height:44px;border-radius:50%;background:var(--brown-light)}
.brand-name{font-family:"Roboto",Arial,sans-serif;font-weight:700;font-size:15px;letter-spacing:.5px;color:var(--brown);text-transform:uppercase}
.main-nav{left:339px;top:61px;display:flex;gap:18px;font-size:12.5px;color:var(--nav);text-transform:uppercase;letter-spacing:.1px}
.btn-small{left:840px;top:9px;width:103px;height:25px;border-radius:13px;
  background:linear-gradient(#a0612a,var(--brown-dark));color:#fff;font-family:"Roboto Condensed",Arial,sans-serif;
  font-weight:700;font-size:10.5px;display:flex;align-items:center;justify-content:center;text-transform:uppercase}
.country{left:948px;top:12px;width:93px;height:19px;border:1px solid #bbb;background:#fff;font-size:10px;font-style:italic;
  padding:3px 8px;color:#333}
.country svg{position:absolute;right:5px;top:6px}
.search{left:891px;top:52px;width:150px;height:27px;border-radius:14px;background:#fff;border:1px solid #d8e8f2}
.search svg{position:absolute;right:10px;top:6px}

/* hero */
.hero-frame{left:150px;top:134px;width:900px;height:360px;background:var(--beige);border-radius:10px}
.hero-inner{left:159px;top:143px;width:882px;height:350px;background:#fff;border-radius:4px}
.hero-photo{left:609px;top:143px;width:432px;height:335px;border-radius:0 4px 0 0;
  background:linear-gradient(90deg,#fff 0%,rgba(240,214,170,.6) 14%,#e6b37e 40%,#c88358 65%,#e8d2b4 100%)}
.hero-title{left:178px;top:220px;font-family:"Roboto Condensed",Arial,sans-serif;font-weight:700;font-size:30px;color:var(--navy);letter-spacing:-.3px}
.hero-sub{left:178px;top:263px;width:440px;font-style:italic;font-weight:300;font-size:17px;line-height:22px;color:#222}
.btn{top:336px;width:169px;height:44px;border-radius:22px;color:#fff;font-weight:700;font-size:12.5px;
  display:flex;align-items:center;justify-content:center;text-transform:uppercase;box-shadow:0 4px 3px rgba(0,0,0,.15)}
.btn-share{left:183px;background:linear-gradient(#b0743d,var(--brown-dark))}
.btn-read{left:361px;background:linear-gradient(#0a93df,var(--blue-dark))}

.wave{left:0;width:1200px}

/* columns */
.col{top:515px;width:262px}
.col-head{display:flex;align-items:center;gap:10px;height:24px}
.col-head h2{font-family:"Roboto Condensed",Arial,sans-serif;font-weight:700;font-size:19.5px;color:var(--brown);white-space:nowrap}
.col-head sup{font-size:10px}
.col-head .rule{flex:1;height:1px;background:var(--rule)}
.col p{margin-top:16px;font-size:12.4px;line-height:18.75px;font-weight:300;color:#222}
.learn{display:block;text-align:right;font-weight:700;font-size:10.5px;color:var(--nav);text-transform:uppercase;margin-top:2px}
.news-item{margin-top:10px}
.news-item:first-of-type{margin-top:14px}
.news-date{font-size:10.5px;font-style:italic;color:#222}
.news-title{display:block;font-size:12.6px;font-weight:700;line-height:18.75px;color:#111;text-decoration:underline;text-decoration-color:#bbb;text-underline-offset:3px}

/* footer */
.social{left:966px;top:786px;display:flex;gap:4px}
.social span{width:15px;height:15px;border-radius:2px}
.footer-links{right:159px;top:808px;font-size:9.5px;color:var(--nav);text-transform:uppercase;word-spacing:1px}
</style>
</head>
<body>

<div class="abs header-band"></div>
<div class="abs brand"><span class="brand-mark"></span><span class="brand-name">Bright Returns</span></div>
<nav class="abs main-nav"><span>About us</span><span>Personal stories</span><span>Tips for living</span><span>News</span><span>Resources</span><span>Contact us</span></nav>
<div class="abs btn-small">&gt;&nbsp; Share a story</div>
<div class="abs country">Australia
  <svg width="9" height="6" viewBox="0 0 9 6"><path d="M1 1l3.5 3.5L8 1" fill="none" stroke="#333" stroke-width="1.3"/></svg></div>
<div class="abs search">
  <svg width="14" height="14" viewBox="0 0 14 14"><circle cx="5.5" cy="5.5" r="4" fill="none" stroke="#bbb" stroke-width="2"/><path d="M8.5 8.5l4 4" stroke="#bbb" stroke-width="2.4" stroke-linecap="round"/></svg></div>

<div class="abs hero-frame"></div>
<div class="abs hero-inner"></div>
<div class="abs hero-photo" role="img" aria-label="Sunlit photo of a smiling mother holding her baby close"></div>
<h1 class="abs hero-title">Sharing Stories &amp; Giving Hope!</h1>
<p class="abs hero-sub">To people around the world whoa re facing inflammatory bowel disease, colorectal cancer, or have had ostomy surgery.</p>
<div class="abs btn btn-share">&gt;&nbsp;&nbsp;Share a story</div>
<div class="abs btn btn-read">&gt;&nbsp;&nbsp;Read stories</div>

<svg class="abs wave" style="top:400px" width="1200" height="200" viewBox="0 0 1200 200">
  <defs><linearGradient id="greenFade" x1="0" y1="0" x2="0" y2="1">
    <stop offset="0" stop-color="#c6e8a2"/><stop offset=".45" stop-color="#eef8e0"/><stop offset="1" stop-color="#fff"/></linearGradient></defs>
  <path d="M0 33 C300 15 480 70 760 80 C950 86 1100 60 1200 25 V200 H0Z" fill="#bfe39a"/>
  <path d="M0 42 C300 24 480 78 760 88 C950 94 1100 68 1200 35 V200 H0Z" fill="url(#greenFade)"/>
</svg>

<section class="abs col" style="left:169px">
  <div class="col-head"><h2>Bright Returns<sup>®</sup></h2><span class="rule"></span>
    <svg width="22" height="18" viewBox="0 0 22 18"><circle cx="11" cy="9" r="7" fill="var(--brown-light)"/></svg></div>
  <p>Lorem ipsum dolor sit amet, consectetur adipiscing elit. Praesent faucibus sem turpis, eget convallis justo feugiat sed. Curabitur interdum risus nulla, id tempus erat laoreet condimentum. Duis rutrum nulla ultrices tellus sagittis, eget vestibulum eros ullamcorper. Aliquam ut est sit amet felis congue varius. Donec tempus nec mauris eu euismod. Donec sem neque, ultrices eget lobortis in, pretium pulvinar lectus.</p>
  <span class="learn">&gt;&nbsp; Learn more</span>
</section>

<section class="abs col" style="left:469px">
  <div class="col-head"><h2>Share a Story!</h2><span class="rule"></span>
    <svg width="17" height="15" viewBox="0 0 17 15"><path d="M8.5 14L2 7.5A3.8 3.8 0 0 1 8.5 2.5 3.8 3.8 0 0 1 15 7.5Z" fill="var(--brown)"/></svg></div>
  <p>Nullam magna elit, laoreet eget tempus porta, volutpat et arcu. Donec nunc sapien, lobortis eu cursus ut, sodales id erat. Quisque sodales purus at magna laoreet eleifend. Nulla accumsan quis erat a fermentum. Fusce eu malesuada ligula, sodales gravida sapien. Etiam non massa sed nulla volutpat tincidunt at vitae libero. Pellentesque habitant morbi tristique senectus et netus et malesuada fames ac turpis egestas.</p>
  <span class="learn">&gt;&nbsp; Learn more</span>
</section>

<section class="abs col" style="left:769px">
  <div class="col-head"><h2>News</h2><span class="rule"></span>
    <svg width="22" height="17" viewBox="0 0 22 17"><rect x="1" y="1" width="20" height="15" fill="none" stroke="var(--brown)" stroke-width="1.8"/><rect x="4" y="4" width="6" height="5" fill="var(--brown)"/><path d="M12 5h6M12 8h6M4 12h14" stroke="var(--brown)" stroke-width="1.4"/></svg></div>
  <div class="news-item"><div class="news-date">// &nbsp;August 21, 2013</div>
    <span class="news-title">Bright Returns® Recognizes Former Principal, Martin Ellsworth, As National Award Recipient</span></div>
  <div class="news-item"><div class="news-date">// &nbsp;May 22, 2013</div>
    <span class="news-title">A Message from Owen Castellan</span></div>
  <div class="news-item"><div class="news-date">// &nbsp;November 21, 2012</div>
    <span class="news-title">Martin Ellsworth of Fairhaven, MD Receives 2012 Bright Returns® East Region Award</span></div>
</section>

<svg class="abs wave" style="top:740px" width="1200" height="107" viewBox="0 0 1200 107">
  <defs><linearGradient id="skyFade" x1="0" y1="0" x2="0" y2="1">
    <stop offset="0" stop-color="#e3f2fa"/><stop offset="1" stop-color="#f8fcfe"/></linearGradient></defs>
  <path d="M0 8 C150 60 300 75 500 60 C750 40 950 15 1200 30 V107 H0Z" fill="#cfe8f6"/>
  <path d="M0 30 C150 72 320 86 520 72 C760 55 960 28 1200 45 V107 H0Z" fill="url(#skyFade)"/>
</svg>

<div class="abs social" aria-label="Social links">
  <span style="background:#3b5998"></span><span style="background:#3aa8e0"></span><span style="background:#1a6aa8"></span><span style="background:#d34836"></span>
</div>
<div class="abs footer-links">Legal notice &nbsp;|&nbsp; Privacy policy &nbsp;|&nbsp; Stemap &nbsp;|&nbsp; <span style="text-transform:none">©2014 Bright Returns®.</span></div>

</body>
</html>
```